Drug safety monitoring company requires a new corporate website

We are an outsourcing partner to large and small companies within the pharmaceutical industry. Our current website www.quorvanta.co.uk has not been updated in a long time. We want a new web site that is responsive and modern but with a clearly corporate and professional feel. We want a design based on a 12 column grid system (mobile and desktop version). We want to use a new, modern font (not the standard web fonts) - we will purchase as required. Content can be used as is from the current website. Red and white are the corporate colours, so a palate should be developed to match. We do not need as much red as is in the current website. New icons (preferably in svg format) would be great. We can also purchase new images from Framly (or other) as required. We would prefer submissions in Sketch if possible.

Target Market(s)

Pharmaceutical companies

Number of Pages Required

1 page

Font styles to use
Sans Serif

Colors
ec1f27
ffffff

Requirements
Must have
• Design based on 12 column grid system.
Responsive design (i.e. require a mobile and desktop version).
How should the menu look between desktop and mobile?
A coherent colour palete.
Content to come from the existing website: www.quorvanta.co.uk
How should links be styled?
How should headings, sub-headings, paragraphs be styled?
Nice to have
• Custom developed icons (these are along the bottom of the page on the existing website: Medical Information; Pharmacovigilance; Literature Monitoring; Training).
New imagery (the images on the current website are dated).
Submission ideally as Sketch files (but we are okay with photoshop too).
A new, modern, non-standard font.
Not so much red in the design.
If we had buttons on the website, how should they be styled?
If we had a form on the website, how should the fields be styled?

```html
<!DOCTYPE html>
<html lang="en">
<head>
<meta charset="utf-8">
<title>Quorvanta Pharmacovigilance – Website Proposal</title>
<link href="https://fonts.googleapis.com/css2?family=Montserrat:ital,wght@0,300;0,400;0,500;0,700;0,800;1,400;1,700&display=swap" rel="stylesheet">
<style>
:root{
  --red:#f20d12;
  --red-deep:#ec1f27;
  --white:#ffffff;
  --ink:#2b2b2b;
  --muted:#8a8a8a;
  --paper:#f3f3f3;
  --card-line:#e6e6e6;
  --panel-top:#b0a9d9;
  --panel-bottom:#f3c5c6;
  --hero-light:#e4dfdc;
  --hero-mid:#c9c1bc;
  --hero-dark:#a39b96;
  --grid-col:rgba(255,110,215,.33);
}
*{box-sizing:border-box;margin:0;padding:0}
html,body{width:1200px;height:1200px;overflow:hidden;background:var(--white)}
body{position:relative;font-family:'Montserrat',sans-serif;color:var(--ink)}

/* ---------- proposal panel ---------- */
.proposal{position:absolute;left:0;top:0;width:292px;height:1200px;
  background:linear-gradient(180deg,var(--panel-top) 0%,#c9b3d3 45%,var(--panel-bottom) 100%)}
.proposal-text{position:absolute;left:32px;top:292px;width:228px;color:var(--white);
  font-weight:400;font-size:18.5px;line-height:22px;letter-spacing:.2px}
.proposal-text p{margin-bottom:21px}

/* ---------- shared brand ---------- */
.brand{display:inline-flex;align-items:center;gap:4px;font-weight:700;letter-spacing:1.2px;white-space:nowrap}
.brand-dot{display:inline-block;border-radius:50%;background:currentColor}

/* ---------- desktop site ---------- */
.frame{position:absolute;box-shadow:0 4px 14px rgba(0,0,0,.12);overflow:hidden;background:var(--white)}
.frame-desktop{left:316px;top:57px;width:597px;height:755px}
.site-desktop{position:relative;width:597px;height:755px;background:var(--white)}
.site-desktop .nav{position:absolute;left:0;top:0;width:100%;height:39px;background:var(--red)}
.site-desktop .nav .brand{position:absolute;left:128px;top:14px;color:var(--white);font-size:7px}
.site-desktop .nav .brand-dot{width:5px;height:5px}
.site-desktop .menu{position:absolute;left:232px;top:16px;width:248px;display:flex;justify-content:space-between;list-style:none}
.site-desktop .menu li{color:var(--white);font-weight:700;font-size:6.2px;letter-spacing:.1px}
.site-desktop .hero{position:absolute;left:0;top:39px;width:100%;height:247px;
  background:linear-gradient(120deg,var(--hero-mid) 0%,var(--hero-light) 40%,var(--hero-mid) 70%,var(--hero-dark) 100%)}
.site-desktop .hero-title{position:absolute;left:0;right:0;top:116px;text-align:center;color:var(--white);
  font-weight:700;font-size:6.4px;line-height:8px;text-shadow:0 0 3px rgba(0,0,0,.3)}
.btn{display:flex;align-items:center;justify-content:center;background:var(--red);color:var(--white);
  border:1px solid var(--white);font-weight:800;text-transform:uppercase;letter-spacing:.2px}
.site-desktop .hero .btn{position:absolute;left:272px;top:145px;width:52px;height:13px;font-size:4.2px}
.site-desktop .intro-brand{position:absolute;left:0;right:0;top:309px;display:flex;justify-content:center}
.site-desktop .intro-brand .brand{color:var(--red);font-size:10px;font-weight:500;letter-spacing:2px}
.site-desktop .intro-brand .brand-dot{width:7px;height:7px}
.site-desktop .intro-copy{position:absolute;left:124px;top:355px;width:349px;font-size:5.1px;line-height:7.8px;color:var(--ink)}
.site-desktop .intro-copy p{margin-bottom:7.8px}
.site-desktop .services{position:absolute;left:0;top:511px;width:100%;height:169px;background:var(--paper)}
.site-desktop .cards{position:absolute;left:117px;top:30px;display:flex;gap:9px}
.site-desktop .card{width:84px;height:109px;background:var(--white);border:1px solid var(--card-line);text-align:center;padding-top:14px}
.site-desktop .card svg{width:24px;height:20px}
.site-desktop .card h3{margin-top:6px;color:var(--red);font-weight:800;font-size:4.4px;line-height:7.5px;text-transform:uppercase;height:17px;display:flex;align-items:center;justify-content:center}
.site-desktop .card p{margin:8px 7px 0;color:var(--muted);font-size:4.3px;line-height:7.4px}
.site-desktop .footer{position:absolute;left:0;top:680px;width:100%;height:75px;background:var(--red);color:var(--white)}
.site-desktop .footer .brand{position:absolute;left:153px;top:19px;font-size:5px}
.site-desktop .footer .brand-dot{width:4px;height:4px}
.site-desktop .footer .legal{position:absolute;left:148px;top:41px;font-size:3.8px;line-height:7.6px}
.site-desktop .footer h4{position:absolute;font-weight:500;font-size:4.3px;top:21px}
.site-desktop .footer .links{position:absolute;top:33px;list-style:none;font-size:3.8px;line-height:7.6px;font-weight:300}
.site-desktop .footer .phone{position:absolute;left:427px;top:33px;font-size:4px}

/* ---------- grid preview ---------- */
.frame-grid{left:658px;top:827px;width:255px;height:323px}
.frame-grid .scaler{transform:scale(.4271);transform-origin:0 0;position:absolute;left:0;top:0}
.grid-overlay{position:absolute;left:124px;top:0;width:349px;height:755px;display:flex;gap:6px}
.grid-overlay span{flex:1;background:var(--grid-col)}

/* ---------- mobile site ---------- */
.frame-mobile{left:932px;top:57px;width:253px;height:1093px}
.site-mobile{position:relative;width:253px;height:1093px}
.site-mobile .nav{position:absolute;left:0;top:0;width:100%;height:44px;background:var(--red)}
.site-mobile .nav .brand{position:absolute;left:39px;top:16px;color:var(--white);font-size:7.5px}
.site-mobile .nav .brand-dot{width:5px;height:5px}
.burger{position:absolute;left:191px;top:10px;width:30px;height:24px}
.burger span{position:absolute;right:0;height:2.6px;border-radius:2px;background:var(--white)}
.burger span:nth-child(1){top:0;width:28px}
.burger span:nth-child(2){top:10px;width:22px}
.burger span:nth-child(3){top:20px;width:18px}
.site-mobile .hero{position:absolute;left:0;top:44px;width:100%;height:220px;
  background:linear-gradient(120deg,var(--hero-mid) 0%,var(--hero-light) 40%,var(--hero-mid) 70%,var(--hero-dark) 100%)}
.site-mobile .hero-title{position:absolute;left:26px;right:26px;top:102px;text-align:center;color:var(--white);
  font-weight:700;font-size:8.6px;line-height:10px;text-shadow:0 0 3px rgba(0,0,0,.3)}
.site-mobile .hero .btn{position:absolute;left:97px;top:154px;width:59px;height:14px;font-size:4.8px}
.site-mobile .intro-brand{position:absolute;left:0;right:0;top:275px;display:flex;justify-content:center}
.site-mobile .intro-brand .brand{color:var(--red);font-size:10px;font-weight:500;letter-spacing:2px}
.site-mobile .intro-brand .brand-dot{width:7px;height:7px}
.site-mobile .intro-copy{position:absolute;left:33px;top:325px;width:192px;font-size:5.8px;line-height:8.3px;letter-spacing:-.05px;color:var(--ink)}
.site-mobile .intro-copy p{margin-bottom:8.3px}
.site-mobile .services{position:absolute;left:0;top:611px;width:100%;height:294px;background:var(--paper)}
.site-mobile .cards{position:absolute;left:31px;top:27px;width:192px;display:grid;grid-template-columns:90px 90px;column-gap:11px;row-gap:10px}
.site-mobile .card{height:117px;background:var(--white);border:1px solid var(--card-line);text-align:center;padding-top:16px}
.site-mobile .card svg{width:26px;height:22px}
.site-mobile .card h3{margin-top:7px;color:var(--red);font-weight:800;font-size:5px;line-height:8px;text-transform:uppercase;height:17px;display:flex;align-items:center;justify-content:center}
.site-mobile .card p{margin:9px 6px 0;color:var(--muted);font-size:4.7px;line-height:8px}
.site-mobile .footer{position:absolute;left:0;top:905px;width:100%;height:188px;background:var(--red);color:var(--white)}
.site-mobile .footer h4{position:absolute;left:33px;font-weight:500;font-size:7.3px;letter-spacing:.4px}
.site-mobile .footer .links{position:absolute;left:33px;top:41px;width:190px;display:grid;grid-template-columns:100px 90px;list-style:none;font-size:6.6px;line-height:12.5px;font-weight:300;color:#ffd9da}
.site-mobile .footer .phone{position:absolute;left:34px;top:117px;font-size:7px}
.site-mobile .footer .legal{position:absolute;left:34px;top:155px;font-size:6.4px;line-height:12.5px}

.icon-defs{position:absolute;width:0;height:0}
</style>
</head>
<body>

<svg class="icon-defs" aria-hidden="true">
  <defs>
    <symbol id="icon-medical" viewBox="0 0 40 32">
      <g fill="none" stroke="#f20d12" stroke-width="1.2" stroke-linecap="round" stroke-linejoin="round">
        <rect x="3" y="15" width="20" height="9" rx="4.5"/>
        <line x1="13" y1="15" x2="13" y2="24"/>
        <circle cx="28" cy="12" r="7"/>
        <line x1="28" y1="5" x2="28" y2="19"/>
      </g>
    </symbol>
    <symbol id="icon-pv" viewBox="0 0 40 32">
      <g fill="none" stroke="#f20d12" stroke-width="1.2" stroke-linecap="round" stroke-linejoin="round">
        <path d="M20 29 L7 16 A7 7 0 0 1 20 7 A7 7 0 0 1 33 16 Z"/>
        <polyline points="9,17 15,17 17,12 20,22 23,14 25,17 31,17"/>
      </g>
    </symbol>
    <symbol id="icon-lit" viewBox="0 0 40 32">
      <g fill="none" stroke="#f20d12" stroke-width="1.2" stroke-linecap="round" stroke-linejoin="round">
        <rect x="12" y="3" width="18" height="25" rx="1"/>
        <path d="M10 6 V30 H27"/>
        <line x1="16" y1="9" x2="26" y2="9"/>
        <line x1="16" y1="13" x2="26" y2="13"/>
        <line x1="16" y1="17" x2="26" y2="17"/>
        <line x1="16" y1="21" x2="23" y2="21"/>
      </g>
    </symbol>
    <symbol id="icon-training" viewBox="0 0 40 32">
      <g fill="none" stroke="#f20d12" stroke-width="1.2" stroke-linecap="round" stroke-linejoin="round">
        <path d="M9 6 L13 5 L15 11 L12 13 Q14 19 19 22 L21 19 L27 22 L26 26 Q14 27 9 6 Z"/>
        <path d="M18 4 Q18 12 24 12 Q30 12 30 4"/>
        <path d="M30 8 Q35 8 35 14"/>
        <circle cx="35" cy="16" r="1.6"/>
      </g>
    </symbol>
  </defs>
</svg>

<aside class="proposal">
  <div class="proposal-text">
    <p>Proposal of a design for your website, based on a Bootstrap grid.</p>
    <p>Can be quickly integrated with Bootstrap.</p>
    <p>Possibility to retouch / review the blocks together + the other pages of the site.</p>
    <p>Thank you for you time to see my work.</p>
    <p>I’m at your disposal for any request, do not hesitate to contact me again.</p>
  </div>
</aside>

<div class="frame frame-desktop">
  <div class="site-desktop">
    <header class="nav">
      <span class="brand"><span class="brand-dot"></span>QUORVANTA</span>
      <ul class="menu"><li>HOME</li><li>ABOUT US</li><li>QPPV</li><li>OUR SERVICES</li><li>CONTACT US</li><li>CLIENT</li></ul>
    </header>
    <section class="hero" role="img" aria-label="Laboratory photograph of a scientist at work">
      <h1 class="hero-title">At Quorvanta we ensure that your business<br>has the best Pharmacovigilance support in the industry</h1>
      <span class="btn">Learn more</span>
    </section>
    <div class="intro-brand"><span class="brand"><span class="brand-dot"></span>QUORVANTA</span></div>
    <div class="intro-copy">
      <p>Welcome to the <b>Quorvanta Pharmacovigilance</b> website. We are an <b>outsourcing partner</b> to large and small companies within the <b>pharmaceutical industry</b>. Our range of services is tailored to suit each of our client’s needs and cover both <b>human and veterinary</b> medicinal products.</p>
      <p><b>Pharmacovigilance</b> is defined by WHO as <i>‘The science and activities relating to the detection, assessment, understanding and <b>prevention of adverse effects</b> or any other drug-related problems’.</i> The process is one of <b>managing risk</b> associated with <b>medicinal products</b>, in an effort to promote their <b>safe and effective</b> use by prescribers and patients.</p>
      <p>Our <b>primary functions</b> are EU <b>QPPV</b> and related <b>pharmacovigilance services</b> to assist and support Marketing Authorisation Holders (MAH), of pharmaceutical product licences, in their efforts to remain compliant with <b>EU regulatory</b> requirements (Regulation 1235/2010 and Directive 2010/84/EU) the deadline for which implementing ended on 21 July 2012.</p>
      <p>The regulatory environment is an ever-changing and evolving one. <b>Legislation is global</b> and the management of this process is complex, requiring a <b>strong relationship</b> between Marketing Authorisation Holders and their QPPV.</p>
      <p><b>Good Pharmacovigilance Practice</b> is dependant on a sound understanding of the key principles of this science and the ability to apply this knowledge competently on behalf of the client.</p>
    </div>
    <section class="services">
      <div class="cards">
        <article class="card"><svg><use href="#icon-medical"/></svg><h3>Medical<br>Information</h3><p>Professional enquiry handling to support the safe and effective use of your products.</p></article>
        <article class="card"><svg><use href="#icon-pv"/></svg><h3>Pharmacovigilance</h3><p>Ease the regulatory burden and keep compliant with current pharmacovigilance legislation.</p></article>
        <article class="card"><svg><use href="#icon-lit"/></svg><h3>Literature<br>Monitoring</h3><p>Product safety through surveillance of published articles and case reports.</p></article>
        <article class="card"><svg><use href="#icon-training"/></svg><h3>Training</h3><p>Confident staff to support the pharmacovigilance process.</p></article>
      </div>
    </section>
    <footer class="footer">
      <span class="brand"><span class="brand-dot"></span>QUORVANTA</span>
      <p class="legal">Copyright © 2020 Quorvanta Ltd<br>(Registered in England &amp; Wales : 08164203)</p>
      <h4 style="left:272px">OUR SERVICES</h4>
      <ul class="links" style="left:272px"><li>Eudravigilance</li><li>Pharmacovigilance</li><li>Medical Information</li></ul>
      <ul class="links" style="left:334px"><li>Literature Monitoring</li><li>Medical Devices</li><li>Training</li></ul>
      <h4 style="left:427px">CONTACT US</h4>
      <p class="phone">0330 482 7190</p>
    </footer>
  </div>
</div>

<div class="frame frame-grid">
  <div class="scaler">
    <div class="site-desktop">
      <header class="nav">
        <span class="brand"><span class="brand-dot"></span>QUORVANTA</span>
        <ul class="menu"><li>HOME</li><li>ABOUT US</li><li>QPPV</li><li>OUR SERVICES</li><li>CONTACT US</li><li>CLIENT</li></ul>
      </header>
      <section class="hero" role="img" aria-label="Laboratory photograph of a scientist at work">
        <h1 class="hero-title">At Quorvanta we ensure that your business<br>has the best Pharmacovigilance support in the industry</h1>
        <span class="btn">Learn more</span>
      </section>
      <div class="intro-brand"><span class="brand"><span class="brand-dot"></span>QUORVANTA</span></div>
      <div class="intro-copy">
        <p>Welcome to the <b>Quorvanta Pharmacovigilance</b> website. We are an <b>outsourcing partner</b> to large and small companies within the <b>pharmaceutical industry</b>. Our range of services is tailored to suit each of our client’s needs and cover both <b>human and veterinary</b> medicinal products.</p>
        <p><b>Pharmacovigilance</b> is defined by WHO as <i>‘The science and activities relating to the detection, assessment, understanding and <b>prevention of adverse effects</b> or any other drug-related problems’.</i> The process is one of <b>managing risk</b> associated with <b>medicinal products</b>, in an effort to promote their <b>safe and effective</b> use by prescribers and patients.</p>
        <p>Our <b>primary functions</b> are EU <b>QPPV</b> and related <b>pharmacovigilance services</b> to assist and support Marketing Authorisation Holders (MAH), of pharmaceutical product licences, in their efforts to remain compliant with <b>EU regulatory</b> requirements (Regulation 1235/2010 and Directive 2010/84/EU) the deadline for which implementing ended on 21 July 2012.</p>
        <p>The regulatory environment is an ever-changing and evolving one. <b>Legislation is global</b> and the management of this process is complex, requiring a <b>strong relationship</b> between Marketing Authorisation Holders and their QPPV.</p>
        <p><b>Good Pharmacovigilance Practice</b> is dependant on a sound understanding of the key principles of this science and the ability to apply this knowledge competently on behalf of the client.</p>
      </div>
      <section class="services">
        <div class="cards">
          <article class="card"><svg><use href="#icon-medical"/></svg><h3>Medical<br>Information</h3><p>Professional enquiry handling to support the safe and effective use of your products.</p></article>
          <article class="card"><svg><use href="#icon-pv"/></svg><h3>Pharmacovigilance</h3><p>Ease the regulatory burden and keep compliant with current pharmacovigilance legislation.</p></article>
          <article class="card"><svg><use href="#icon-lit"/></svg><h3>Literature<br>Monitoring</h3><p>Product safety through surveillance of published articles and case reports.</p></article>
          <article class="card"><svg><use href="#icon-training"/></svg><h3>Training</h3><p>Confident staff to support the pharmacovigilance process.</p></article>
        </div>
      </section>
      <footer class="footer">
        <span class="brand"><span class="brand-dot"></span>QUORVANTA</span>
        <p class="legal">Copyright © 2020 Quorvanta Ltd<br>(Registered in England &amp; Wales : 08164203)</p>
        <h4 style="left:272px">OUR SERVICES</h4>
        <ul class="links" style="left:272px"><li>Eudravigilance</li><li>Pharmacovigilance</li><li>Medical Information</li></ul>
        <ul class="links" style="left:334px"><li>Literature Monitoring</li><li>Medical Devices</li><li>Training</li></ul>
        <h4 style="left:427px">CONTACT US</h4>
        <p class="phone">0330 482 7190</p>
      </footer>
      <div class="grid-overlay" aria-hidden="true">
        <span></span><span></span><span></span><span></span><span></span><span></span>
        <span></span><span></span><span></span><span></span><span></span><span></span>
      </div>
    </div>
  </div>
</div>

<div class="frame frame-mobile">
  <div class="site-mobile">
    <header class="nav">
      <span class="brand"><span class="brand-dot"></span>QUORVANTA</span>
      <div class="burger" aria-label="Menu"><span></span><span></span><span></span></div>
    </header>
    <section class="hero" role="img" aria-label="Laboratory photograph of a scientist at work">
      <h1 class="hero-title">At Quorvanta we ensure that your business has the best Pharmacovigilance support in the industry</h1>
      <span class="btn">Learn more</span>
    </section>
    <div class="intro-brand"><span class="brand"><span class="brand-dot"></span>QUORVANTA</span></div>
    <div class="intro-copy">
      <p>Welcome to the <b>Quorvanta Pharmacovigilance</b> website. We are an <b>outsourcing partner</b> to large and small companies within the <b>pharmaceutical industry</b>. Our range of services is tailored to suit each of our client’s needs and cover both <b>human and veterinary</b> medicinal products.</p>
      <p><b>Pharmacovigilance</b> is defined by WHO as <i>‘The science and activities relating to the detection, assessment, understanding and <b>prevention of adverse effects</b> or any other drug-related problems’.</i> The process is one of <b>managing risk</b> associated with <b>medicinal products</b>, in an effort to promote their <b>safe and effective</b> use by prescribers and patients.</p>
      <p>Our <b>primary functions</b> are EU <b>QPPV</b> and related <b>pharmacovigilance services</b> to assist and support Marketing Authorisation Holders (MAH), of pharmaceutical product licences, in their efforts to remain compliant with <b>EU regulatory</b> requirements (Regulation 1235/2010 and Directive 2010/84/EU) the deadline for which implementing ended on 21 July 2012.</p>
      <p>The regulatory environment is an ever-changing and evolving one. <b>Legislation is global</b> and the management of this process is complex, requiring a <b>strong relationship</b> between Marketing Authorisation Holders and their QPPV.</p>
      <p><b>Good Pharmacovigilance Practice</b> is dependant on a sound understanding of the key principles of this science and the ability to apply this knowledge competently on behalf of the client.</p>
    </div>
    <section class="services">
      <div class="cards">
        <article class="card"><svg><use href="#icon-medical"/></svg><h3>Medical<br>Information</h3><p>Professional enquiry handling to support the safe and effective use of your products.</p></article>
        <article class="card"><svg><use href="#icon-pv"/></svg><h3>Pharmacovigilance</h3><p>Ease the regulatory burden and keep compliant with current pharmacovigilance legislation.</p></article>
        <article class="card"><svg><use href="#icon-lit"/></svg><h3>Literature<br>Monitoring</h3><p>Product safety through surveillance of published articles and case reports.</p></article>
        <article class="card"><svg><use href="#icon-training"/></svg><h3>Training</h3><p>Confident staff to support the pharmacovigilance process.</p></article>
      </div>
    </section>
    <footer class="footer">
      <h4 style="top:22px">OUR SERVICES</h4>
      <ul class="links">
        <li>Eudravigilance</li><li>Literature Monitoring</li>
        <li>Pharmacovigilance</li><li>Medical Devices</li>
        <li>Medical Information</li><li>Training</li>
      </ul>
      <h4 style="top:97px">CONTACT US</h4>
      <p class="phone">0330 482 7190</p>
      <p class="legal">Copyright © 2020 Quorvanta Ltd<br>(Registered in England &amp; Wales : 08164203)</p>
    </footer>
  </div>
</div>

</body>
</html>
```